Personal training poster

Hi, I need a poster designed for my personal training business to help attracted some new clients over these quiet months. I want the poster to be eye catching and something that I can put up in the gym when I need to attract some new business, so it can no be seasional (i.e) Winter, Summer reference.

My logo has to be includes (Calloway Strength & Nutrition)

Target Market(s)

New clients within a gym envitoment

Industry/Entity Type

Fitness

Font styles to use
Serif

Colors

Designer to choose colors to be used in the design.

Requirements
Must have
• My Logo
• Personal training introductory offer 4 X 45min sessions $180
• STOP WISHING. START DOING.
• Want to loose weight and or build muscle?
• Want to feel healthier and fitter
• Want to learn proper/safe techique?
• Please contact Dale @ callowaystrength@examplemail.net or phone 0472815094
• *conditions apply at the bottom
Nice to have
• My facebook and instagram
• calloway_strength_nutrition (instagram)
• Calloway Strength & Nutrition (facebook)
• Eat Clean, Train Dirty
Should not have
• Imiges of Femaile trainers as I am a Male

```html
<!DOCTYPE html>
<html lang="en">
<head>
<meta charset="utf-8">
<title>Personal Training Poster – Calloway Strength & Nutrition</title>
<link href="https://fonts.googleapis.com/css2?family=Oswald:wght@400;500;600&family=Roboto+Condensed:wght@400;700&display=swap" rel="stylesheet">
<style>
  :root {
    --page-bg: #e6e6e6;
    --poster-black: #0c0c0c;
    --photo-dark: #1c1c1c;
    --photo-mid: #5a5a5a;
    --photo-light: #9a9a9a;
    --brand-red: #c1121f;
    --band-red: #a90f1b;
    --band-red-shadow: #5e0a10;
    --band-grey: #6d6d6d;
    --text-white: #ffffff;
    --text-grey: #a8a8a8;
    --panel-grey: rgba(70, 70, 70, 0.85);
    --footer-grey: #2a2a2a;
    --social-mark: #5b7fc1;
  }
  * { box-sizing: border-box; margin: 0; padding: 0; }
  html, body {
    width: 1200px; height: 805px; overflow: hidden;
    background: var(--page-bg);
  }
  .poster {
    position: absolute; left: 345px; top: 22px;
    width: 510px; height: 760px;
    background: var(--poster-black);
    overflow: hidden;
    font-family: "Roboto Condensed", "Arial Narrow", sans-serif;
    color: var(--text-white);
  }
  .photo { position: absolute; }
  .photo--trainer {
    left: 230px; top: 0; width: 280px; height: 300px;
    background: radial-gradient(ellipse at 55% 45%, var(--photo-light) 0%, var(--photo-mid) 30%, var(--photo-dark) 65%, var(--poster-black) 100%);
  }
  .photo--client {
    left: 0; top: 430px; width: 260px; height: 290px;
    background: radial-gradient(ellipse at 40% 50%, var(--photo-light) 0%, var(--photo-mid) 30%, var(--photo-dark) 65%, var(--poster-black) 100%);
  }
  .bands { position: absolute; left: 0; top: 0; width: 510px; height: 760px; }
  .headline { position: absolute; left: 35px; font-family: "Oswald", sans-serif; font-weight: 500; line-height: 1; }
  .headline--personal { top: 40px; font-size: 32px; }
  .headline--training { top: 80px; font-size: 46px; }
  .offer-label {
    position: absolute; left: 35px; top: 150px; width: 225px;
    font-family: "Oswald", sans-serif; font-size: 22px; color: var(--text-grey);
    border-top: 2px solid var(--text-grey); border-bottom: 2px solid var(--text-grey);
    line-height: 1.15; letter-spacing: 0.5px; white-space: nowrap;
  }
  .price {
    position: absolute; left: 33px; top: 180px;
    font-family: "Oswald", sans-serif; font-weight: 500; font-size: 62px; line-height: 1;
  }
  .sessions {
    position: absolute; left: 172px; top: 188px;
    font-family: "Oswald", sans-serif; color: var(--brand-red); line-height: 1.15;
  }
  .sessions__count { font-size: 25px; }
  .sessions__count small { font-size: 21px; font-weight: 400; }
  .sessions__label { font-size: 26px; }
  .slogan {
    position: absolute; font-family: "Oswald", sans-serif; line-height: 1.02;
    white-space: nowrap;
  }
  .slogan strong { display: block; font-weight: 600; font-size: 42px; }
  .slogan span { display: block; font-weight: 400; font-size: 34px; }
  .slogan--stop {
    right: 222px; top: 286px; text-align: right;
    transform: rotate(-14deg); transform-origin: right top;
  }
  .slogan--start {
    left: 316px; top: 300px;
    transform: rotate(-12deg); transform-origin: left top;
  }
  .checklist {
    position: absolute; left: 262px; top: 440px; list-style: none;
    font-size: 13px; line-height: 25px; white-space: nowrap;
  }
  .checklist li { display: flex; align-items: center; gap: 5px; }
  .checklist svg { flex: none; }
  .contact {
    position: absolute; left: 262px; top: 526px; width: 246px; height: 84px;
    background: var(--panel-grey); padding: 9px 10px 0 14px;
    font-size: 12px; line-height: 23px; white-space: nowrap;
  }
  .contact b { font-size: 14px; }
  .contact .contact__email { font-size: 13px; }
  .brand-name {
    position: absolute; left: 305px; top: 648px; width: 200px; text-align: center;
    font-family: "Roboto Condensed", sans-serif; font-weight: 700; font-size: 19px;
    color: var(--brand-red); line-height: 1.15;
  }
  .social {
    position: absolute; left: 0; top: 714px; width: 300px; height: 30px;
    background: var(--footer-grey); display: flex; align-items: center; gap: 14px;
    padding: 0 12px; font-size: 10px;
  }
  .social__item { display: flex; align-items: center; gap: 5px; white-space: nowrap; }
  .social__mark { width: 11px; height: 11px; background: var(--social-mark); flex: none; }
  .conditions {
    position: absolute; left: 14px; top: 748px; font-size: 8px; color: var(--text-grey);
  }
</style>
</head>
<body>
  <main class="poster">
    <div class="photo photo--trainer" role="img" aria-label="Black and white photo of a male trainer doing a dumbbell curl"></div>
    <div class="photo photo--client" role="img" aria-label="Black and white photo of a client doing a dumbbell row on a bench"></div>

    <svg class="bands" viewBox="0 0 510 760" aria-hidden="true">
      <polygon points="0,454 302,366 302,380 0,476" fill="var(--band-red-shadow)"/>
      <polygon points="0,345 302,262 302,366 0,454" fill="var(--band-red)"/>
      <polygon points="302,307 508,247 508,350 302,404" fill="var(--band-grey)"/>
    </svg>

    <h1 class="headline headline--personal">PERSONAL</h1>
    <h1 class="headline headline--training">TRAINING</h1>
    <p class="offer-label">INTRODUCTORY OFFER</p>
    <p class="price">$180</p>
    <p class="sessions">
      <span class="sessions__count">4 x 45 <small>MIN</small></span><br>
      <span class="sessions__label">SESSIONS</span>
    </p>

    <p class="slogan slogan--stop"><strong>STOP</strong><span>WISHING</span></p>
    <p class="slogan slogan--start"><strong>START</strong><span>DOING</span></p>

    <ul class="checklist">
      <li><svg width="11" height="11" viewBox="0 0 11 11"><rect x="0.5" y="0.5" width="10" height="10" fill="none" stroke="var(--brand-red)"/><path d="M2 5.5l2.5 2.5L10 1" fill="none" stroke="var(--brand-red)" stroke-width="1.8"/></svg>Want to loose weight &amp; or build muscle?</li>
      <li><svg width="11" height="11" viewBox="0 0 11 11"><rect x="0.5" y="0.5" width="10" height="10" fill="none" stroke="var(--brand-red)"/><path d="M2 5.5l2.5 2.5L10 1" fill="none" stroke="var(--brand-red)" stroke-width="1.8"/></svg>Want to feel healthier &amp; fitter</li>
      <li><svg width="11" height="11" viewBox="0 0 11 11"><rect x="0.5" y="0.5" width="10" height="10" fill="none" stroke="var(--brand-red)"/><path d="M2 5.5l2.5 2.5L10 1" fill="none" stroke="var(--brand-red)" stroke-width="1.8"/></svg>Want to learn proper/safe techique?</li>
    </ul>

    <div class="contact">
      Please contact <b>Dale</b> @<br>
      <b class="contact__email">callowaystrength@examplemail.net</b> or<br>
      Call : <b>+61 472 815 094</b>
    </div>

    <p class="brand-name">Calloway Strength<br>&amp; Nutrition</p>

    <div class="social">
      <span class="social__item"><span class="social__mark"></span>Calloway Strength &amp; Nutrition</span>
      <span class="social__item"><span class="social__mark"></span>calloway_strength_nutrition</span>
    </div>
    <p class="conditions">*conditions apply</p>
  </main>
</body>
</html>
```